Bright Path Flyer Design for Virtual Online Clinic. -5.5 x 8.5 inches (half sheet)

We need a clean, modern flyer design for Bright Path, a new virtual walk-in clinic based in British Columbia. The flyer will be used in libraries, pharmacies, and community centers to help residents easily access primary care through their Bright Path NFC access card.
The flyer will ask a question : NEED A DOCTOR? This should be large and attention grabbing.
The design should clearly feature a Bright Path card image (the access card) as the centerpiece and visually show how patients can use it to book appointments. The tone should feel trustworthy, healthcare-oriented, and community-friendly — clean fonts, clear spacing, and strong readability from a distance.

Side One: This card has the NFC Access Card.
NEED A DOCTOR? (Large Font, Attention Grabbing)
How to Book an Appointment using your Bright Path Card
Step 1: Tap Your Card on Your Phone
Hold your card near the back of your phone.
It will activate automatically — no app needed.
The Bright Path scheduler will open.
Step 2: Schedule Your Appointment
Select your clinical concern.
Choose your time window.
Register (only once).
Confirm your appointment.
Step 3: Relax, we’ll take care of the rest
A doctor will call during your scheduled time.
Once booked, you’ll be able to call our office.
No emails, no texts — just a real person.
It’s that simple.
Side Two:
About Bright Path
Created by Dr. Marcus Ferrigan
Bright Path was founded to make healthcare simple and convenient. Prescription renewals. Common infections. Medical notes. And so much more.
Our doctors can address 120+ health concerns virtually — providing quality care without the waiting room. No waiting rooms. Just real doctors providing real care.
Why Patients Choose Bright Path
Easy access – book and be seen from anywhere in BC.
Effortless booking – tap your Bright Path Card to begin.
Trusted physicians – every visit is with a licensed BC family doctor.
How It Works
Book your visit — choose a time window that fits your day.
Join the queue — you’ll be called when it’s your turn.
Speak directly with your doctor — simple, secure, and stress-free.
Convenient Care for Common Concerns

Additional Details.
Please find the domain to be launched soon. I've attached the NFC card file for review, it is 85.5 mm x 54 mm. The card will be glued to the flyer.
I've attached examples of flyers but they are not the look I am seeking and I am looking for creative solutions.
Thank you!
http://brightpath-example.test/

Adult Patients in British Columbia

Healthcare

• Looking for clean lines, uniform appearance, and high legibility i.e poppins

0054AA
0677BA
7BADD7
CADEEF
E8F1F8

• Need A Doctor?
• Elegant style, not too busy, clear layout.
• Clutter, look cheap - review examples.

```html
<!DOCTYPE html>
<html lang="en">
<head>
<meta charset="utf-8">
<title>Bright Path – Flyer, Side One and Side Two</title>
<link href="https://fonts.googleapis.com/css2?family=Poppins:wght@400;500;600;700;800&display=swap" rel="stylesheet">
<style>
  :root{
    --navy:#0054AA;
    --blue:#0677BA;
    --sky:#7BADD7;
    --mist:#CADEEF;
    --ice:#E8F1F8;
    --teal:#1BA1AB;
    --ink:#141414;
    --body:#2a2a2a;
    --muted:#8a8a8a;
    --card:#2c3f8e;
    --mint:#cfe7dc;
    --blush:#edd8e6;
    --board:#e6e6e6;
    --paper:#ffffff;
  }
  *{margin:0;padding:0;box-sizing:border-box}
  html,body{width:1200px;height:801px;overflow:hidden;background:var(--board)}
  body{position:relative;font-family:"Poppins",sans-serif;color:var(--body)}
  .flyer{position:absolute;background:var(--paper);overflow:hidden;box-shadow:0 1px 3px rgba(0,0,0,.08)}
  .flyer--front{left:103px;top:66px;width:471px;height:667px}
  .flyer--back{left:625px;top:63px;width:475px;height:670px;background:#fbfcfd}

  .corner{position:absolute;border-radius:50%}
  .corner--front-top{width:142px;height:142px;right:-71px;top:-71px;background:var(--navy)}
  .corner--front-bottom{width:64px;height:64px;left:-32px;bottom:-32px;background:var(--teal)}
  .corner--back-top{width:142px;height:142px;left:-71px;top:-71px;background:var(--navy)}

  .brand{position:absolute;left:0;width:100%;text-align:center;font-size:23px;font-weight:500;color:var(--navy);letter-spacing:.2px}
  .brand::after{content:"";display:inline-block;width:9px;height:9px;border-radius:50%;background:var(--navy);margin-left:6px;vertical-align:middle}

  .headline{position:absolute;left:0;top:84px;width:100%;text-align:center;font-weight:800;color:var(--teal);font-size:63px;line-height:55px;letter-spacing:-1px}

  .access-card{position:absolute;left:90px;top:222px;width:290px;height:164px;border-radius:9px;transform:rotate(-3deg);
    background:linear-gradient(135deg,#34489a 0%,var(--card) 55%,#26377f 100%);box-shadow:0 6px 12px rgba(20,30,80,.25)}
  .waves{position:absolute;left:0;top:0}

  .howto{position:absolute;left:0;top:413px;width:100%;text-align:center;font-size:17.5px;font-weight:600;color:var(--ink);line-height:20px}
  .howto em{font-style:normal;color:var(--navy)}

  .step{position:absolute;top:493px;width:140px}
  .step__icon{position:absolute;left:0;top:0;width:32px;height:32px;border-radius:50%;background:var(--navy);display:flex;align-items:center;justify-content:center}
  .step__title{position:absolute;left:38px;top:-1px;font-size:13.5px;font-weight:600;color:var(--ink);white-space:nowrap}
  .step__sub{position:absolute;left:38px;top:17px;font-size:7.8px;font-weight:500;color:var(--teal);line-height:10.5px;white-space:nowrap}
  .step__list{position:absolute;left:10px;top:46px;width:128px;list-style:none;font-size:8.6px;line-height:10.2px;color:var(--body)}
  .step__list li{position:relative;padding-left:11px;margin-bottom:7.5px}
  .step__list li::before{content:"";position:absolute;left:0;top:3.5px;width:4px;height:4px;border-radius:50%;background:var(--teal)}

  .about-title{position:absolute;left:0;top:88px;width:100%;text-align:center;font-size:33px;font-weight:800;color:var(--teal);letter-spacing:-.6px;line-height:40px}
  .about-by{position:absolute;left:0;top:126px;width:100%;text-align:center;font-size:17px;color:var(--ink);line-height:22px}
  .about-by strong{color:var(--navy);font-weight:700}
  .intro{position:absolute;left:44px;width:184px;font-size:10.2px;line-height:14.7px;color:var(--body)}
  .intro strong{color:var(--navy);font-weight:700}
  .card-photo{position:absolute;left:240px;top:162px;width:226px;height:178px;border-radius:4px;
    background:linear-gradient(155deg,#fbfcfd 0%,#eef0f6 35%,#c9d0e6 62%,#4a5ca6 85%,#2c3f8e 100%)}

  .panel{position:absolute;top:382px;height:223px}
  .panel--why{left:0;width:237px;background:var(--mint)}
  .panel--how{left:237px;width:238px;background:var(--blush)}
  .panel__title{position:absolute;top:53px;font-size:11.6px;font-weight:700;color:var(--ink);line-height:14px}
  .banner{position:absolute;left:54px;top:354px;width:361px;height:57px;border-radius:7px;background:var(--blue);color:#fff;text-align:center;font-size:16px;font-weight:600;line-height:19px;padding-top:9px}

  .reason{position:absolute;left:32px;width:180px;padding-left:18px;font-size:9.3px;line-height:12.6px;color:var(--body)}
  .reason svg{position:absolute;left:0;top:0}
  .workstep{position:absolute;left:22px;width:200px}
  .workstep__icon{position:absolute;left:0;top:0;width:29px;height:29px;border-radius:50%;background:var(--navy);display:flex;align-items:center;justify-content:center}
  .workstep__text{position:absolute;left:45px;top:-2px;width:140px;font-size:9.3px;line-height:12.6px;color:var(--body)}
  .workstep__text strong{font-weight:600;color:var(--ink)}

  .tagline{position:absolute;left:0;top:618px;width:100%;text-align:center;font-size:14.5px;font-weight:600;color:var(--blue)}
  .site{position:absolute;left:0;top:641px;width:100%;text-align:center;font-size:10px;color:var(--muted)}
</style>
</head>
<body>

<section class="flyer flyer--front" aria-label="Flyer side one">
  <span class="corner corner--front-top"></span>
  <span class="corner corner--front-bottom"></span>
  <div class="brand" style="top:32px">Bright Path</div>
  <h1 class="headline">NEED A<br>DOCTOR?</h1>

  <svg class="waves" width="471" height="667" viewBox="0 0 471 667" aria-hidden="true">
    <g fill="none" stroke="var(--sky)" stroke-width="5.5" stroke-linecap="round">
      <path d="M60 294 A52 52 0 0 0 70 370"/>
      <path d="M72 302 A38 38 0 0 0 80 359"/>
      <path d="M85 310 A24 24 0 0 0 90 348"/>
      <path d="M412 243 A52 52 0 0 1 403 324"/>
      <path d="M400 251 A38 38 0 0 1 394 312"/>
      <path d="M388 260 A24 24 0 0 1 385 300"/>
    </g>
  </svg>
  <div class="access-card" role="img" aria-label="Photo of the navy Bright Path NFC access card taped to the flyer"></div>

  <h2 class="howto">How to <em>Book an Appointment</em> using<br>your <em>Bright Path Card</em></h2>

  <div class="step" style="left:26px">
    <span class="step__icon"><svg width="14" height="16" viewBox="0 0 14 16"><rect x="3" y="1" width="8" height="14" rx="1.5" fill="none" stroke="#fff" stroke-width="1.4"/><line x1="6" y1="12.5" x2="8" y2="12.5" stroke="#fff" stroke-width="1.2"/></svg></span>
    <div class="step__title">Step 1</div>
    <div class="step__sub">Tap Your Card on<br>Your Phone</div>
    <ul class="step__list">
      <li>Hold your card near the back of your phone.</li>
      <li>It will activate automatically — no app needed.</li>
      <li>The Bright Path scheduler will open.</li>
    </ul>
  </div>
  <div class="step" style="left:164px">
    <span class="step__icon"><svg width="16" height="16" viewBox="0 0 16 16"><rect x="2" y="3" width="12" height="11" rx="2" fill="none" stroke="#fff" stroke-width="1.4"/><line x1="2" y1="6.5" x2="14" y2="6.5" stroke="#fff" stroke-width="1.2"/><line x1="5" y1="1.5" x2="5" y2="4" stroke="#fff" stroke-width="1.4"/><line x1="11" y1="1.5" x2="11" y2="4" stroke="#fff" stroke-width="1.4"/><rect x="5" y="8.5" width="3" height="3" fill="#fff"/></svg></span>
    <div class="step__title">Step 2</div>
    <div class="step__sub">Schedule Your<br>Appointment</div>
    <ul class="step__list">
      <li>Select your clinical concern.</li>
      <li>Choose your time window.</li>
      <li>Register (only once).</li>
      <li>Confirm your appointment.</li>
    </ul>
  </div>
  <div class="step" style="left:319px">
    <span class="step__icon"><svg width="16" height="16" viewBox="0 0 16 16"><circle cx="8" cy="8" r="6" fill="none" stroke="#fff" stroke-width="1.4"/><path d="M8 4.5V8l2.5 1.8" fill="none" stroke="#fff" stroke-width="1.4" stroke-linecap="round"/></svg></span>
    <div class="step__title">Step 3</div>
    <div class="step__sub">Relax, we'll take<br>care of the rest</div>
    <ul class="step__list">
      <li>A doctor will call during your scheduled time.</li>
      <li>Once booked, you'll be able to call our office.</li>
      <li>No emails, no texts — just a real person. It's that simple.</li>
    </ul>
  </div>
</section>

<section class="flyer flyer--back" aria-label="Flyer side two">
  <span class="corner corner--back-top"></span>
  <div class="brand" style="top:34px">Bright Path</div>
  <h1 class="about-title">ABOUT BRIGHT PATH</h1>
  <p class="about-by">Created by <strong>Dr. Marcus Ferrigan</strong></p>

  <div class="card-photo" role="img" aria-label="Photo of two Bright Path access cards, navy front and white back"></div>
  <p class="intro" style="top:167px"><strong>Bright Path</strong> was founded to make healthcare simple and convenient. Prescription renewals. Common infections. Medical notes. And so much more.</p>
  <p class="intro" style="top:255px">Our doctors can <strong>address 120+ health concerns</strong> virtually — providing quality care without the waiting room.</p>

  <div class="panel panel--why">
    <h3 class="panel__title" style="left:32px">Why Patients Choose<br>Bright Path?</h3>
    <p class="reason" style="top:95px"><svg width="12" height="12" viewBox="0 0 12 12"><circle cx="6" cy="6" r="5" fill="none" stroke="#5aa58a" stroke-width="1"/><path d="M3.5 6.2l1.7 1.6 3.3-3.4" fill="none" stroke="#5aa58a" stroke-width="1.1"/></svg>Easy access – book and be seen from anywhere in BC.</p>
    <p class="reason" style="top:129px"><svg width="12" height="12" viewBox="0 0 12 12"><circle cx="6" cy="6" r="5" fill="none" stroke="#5aa58a" stroke-width="1"/><path d="M3.5 6.2l1.7 1.6 3.3-3.4" fill="none" stroke="#5aa58a" stroke-width="1.1"/></svg>Effortless booking – tap your Bright Path Card to begin.</p>
    <p class="reason" style="top:163px"><svg width="12" height="12" viewBox="0 0 12 12"><circle cx="6" cy="6" r="5" fill="none" stroke="#5aa58a" stroke-width="1"/><path d="M3.5 6.2l1.7 1.6 3.3-3.4" fill="none" stroke="#5aa58a" stroke-width="1.1"/></svg>Trusted physicians – every visit is with a licensed BC family doctor.</p>
  </div>

  <div class="panel panel--how">
    <h3 class="panel__title" style="left:23px">How It Works?</h3>
    <div class="workstep" style="top:89px">
      <span class="workstep__icon"><svg width="14" height="14" viewBox="0 0 16 16"><rect x="2" y="3" width="12" height="11" rx="2" fill="none" stroke="#fff" stroke-width="1.5"/><circle cx="8" cy="9" r="2.5" fill="none" stroke="#fff" stroke-width="1.3"/><line x1="5" y1="1.5" x2="5" y2="4" stroke="#fff" stroke-width="1.5"/><line x1="11" y1="1.5" x2="11" y2="4" stroke="#fff" stroke-width="1.5"/></svg></span>
      <p class="workstep__text"><strong>Book your visit</strong> — choose a time window that fits your day.</p>
    </div>
    <div class="workstep" style="top:131px">
      <span class="workstep__icon"><svg width="15" height="14" viewBox="0 0 16 14"><circle cx="6" cy="4.5" r="2.8" fill="none" stroke="#fff" stroke-width="1.3"/><path d="M1 13c0-3 2.2-4.5 5-4.5s5 1.5 5 4.5" fill="none" stroke="#fff" stroke-width="1.3"/><path d="M10.5 2a2.8 2.8 0 0 1 0 5.2M12.5 9c1.5.6 2.5 2 2.5 4" fill="none" stroke="#fff" stroke-width="1.3"/></svg></span>
      <p class="workstep__text"><strong>Join the queue</strong> — you'll be called when it's your turn.</p>
    </div>
    <div class="workstep" style="top:172px">
      <span class="workstep__icon"><svg width="14" height="14" viewBox="0 0 16 16"><circle cx="8" cy="4.5" r="3" fill="none" stroke="#fff" stroke-width="1.4"/><path d="M2 15v-2.5c0-2.5 2.5-4 6-4s6 1.5 6 4V15z" fill="none" stroke="#fff" stroke-width="1.4"/><path d="M8 10.5v2.5M6.8 11.8h2.4" stroke="#fff" stroke-width="1.2"/></svg></span>
      <p class="workstep__text"><strong>Speak directly with your doctor</strong> — simple, secure, and stress-free.</p>
    </div>
  </div>

  <div class="banner">No waiting rooms.<br>Just real doctors providing real care.</div>

  <p class="tagline">Convenient Care for Common Concerns</p>
  <p class="site">www.brightpath-example.test</p>
</section>

</body>
</html>
```